Post card Design 99mm x 210mm

Holiday Park, units, tent sites, powered sites for caravans and motor homes. Flyer needed to distribute to Information centres and other tourist attractions around the country to advertise the Park. I have a logo and the photo of the Kaipara harbour that is on the web site. please advise what else you require

Tourist

```html
<!DOCTYPE html>
<html lang="en">
<head>
<meta charset="utf-8">
<title>Tarewa Holiday Park – Cabins and Camping</title>
<link rel="stylesheet" href="https://fonts.googleapis.com/css2?family=Lato:wght@400;700;900&family=Cabin+Condensed:wght@600&display=swap">
<style>
  :root {
    --brand-blue: #0b4fa6;
    --deep-blue: #083a86;
    --sky-blue: #3f8fd8;
    --heading-blue: #1f62ad;
    --text-dark: #1c1c1c;
    --tagline-blue: #8fd0f2;
    --page-top: #eef3f8;
    --page-bottom: #a8c1d8;
    --swoosh-green: #7dc23c;
    --swoosh-lime: #b6db5a;
    --swoosh-blue: #2a63b8;
    --white: #ffffff;
  }
  * { margin: 0; padding: 0; box-sizing: border-box; }
  html, body { width: 779px; height: 1200px; overflow: hidden; }
  body { background: #ffffff; font-family: "Lato", Arial, sans-serif; }

  .postcard {
    position: relative;
    width: 779px;
    height: 1200px;
    overflow: hidden;
    background: linear-gradient(180deg, var(--page-top) 0%, #d4e1ec 55%, var(--page-bottom) 100%);
  }

  .header-band { position: absolute; left: 0; top: 0; width: 779px; height: 230px; }

  .brand { position: absolute; left: 30px; top: 38px; display: flex; align-items: center; gap: 10px; }
  .brand-dot { width: 44px; height: 44px; border-radius: 50%; background: var(--white); }
  .brand-name {
    color: var(--white);
    font-weight: 700;
    font-size: 29px;
    line-height: 1.0;
  }
  .tagline {
    position: absolute; left: 40px; top: 138px;
    font-family: "Cabin Condensed", "Arial Narrow", sans-serif;
    font-weight: 600; font-size: 27px; color: var(--tagline-blue);
    letter-spacing: -0.2px;
  }

  .contact { position: absolute; left: 431px; top: 56px; color: var(--white); font-weight: 700; font-variant: small-caps; }
  .contact .web { font-size: 15px; letter-spacing: 1px; text-transform: uppercase; }
  .contact .phone { font-size: 17px; margin-top: 4px; letter-spacing: 0.4px; }
  .contact .address { margin-top: 14px; margin-left: 65px; font-size: 15px; line-height: 21px; }

  .photo-column { position: absolute; left: 444px; top: 190px; width: 330px; }
  .photo { display: block; width: 330px; margin-bottom: 4px; }
  .photo-harbour { height: 211px; background: linear-gradient(180deg, #b9cfb8 0%, #6f9a4a 45%, #3f7a2a 100%); }
  .photo-playground { height: 192px; background: linear-gradient(160deg, #8aa6a2 0%, #b08a55 50%, #4f7d33 100%); }
  .photo-cabin { height: 191px; background: linear-gradient(180deg, #9cc3e4 0%, #4f8a3c 45%, #3b7a2c 100%); }
  .photo-campground { height: 179px; background: linear-gradient(180deg, #9ec2de 0%, #6d8c5a 50%, #c9c9c1 100%); }
  .photo-sunset { height: 214px; background: linear-gradient(180deg, #d9461a 0%, #f08a26 45%, #7a2a10 100%); }

  .swoosh { position: absolute; left: 370px; top: 200px; width: 110px; height: 1000px; }

  .attractions { position: absolute; left: 34px; top: 254px; width: 350px; color: var(--text-dark); }
  .attractions h2 {
    color: var(--heading-blue); font-weight: 700; font-size: 19.5px; line-height: 28px;
    text-transform: uppercase; letter-spacing: 0.2px;
  }
  .attractions ul { list-style: none; margin-top: 24px; }
  .attractions li {
    position: relative; padding-left: 36px; font-size: 16.4px; line-height: 26px; margin-bottom: 1px;
  }
  .attractions li::before {
    content: ""; position: absolute; left: 5px; top: 10px; width: 6px; height: 6px;
    background: var(--text-dark); transform: rotate(45deg);
  }

  .closing { position: absolute; left: 34px; top: 912px; width: 345px; font-size: 16.8px; line-height: 28px; color: var(--text-dark); }
  .call-to-action {
    position: absolute; left: 34px; top: 1097px; color: var(--heading-blue);
    font-weight: 700; font-size: 19px; font-variant: small-caps; letter-spacing: 0.5px;
  }
</style>
</head>
<body>
<div class="postcard">

  <svg class="header-band" viewBox="0 0 779 230" aria-hidden="true">
    <defs>
      <linearGradient id="band" x1="0" y1="0" x2="1" y2="0.3">
        <stop offset="0" stop-color="#0b55b3"/>
        <stop offset="0.6" stop-color="#0a4aa0"/>
        <stop offset="1" stop-color="#1e6fc4"/>
      </linearGradient>
      <linearGradient id="haze" x1="0" y1="0" x2="0" y2="1">
        <stop offset="0" stop-color="#6fa7dc"/>
        <stop offset="1" stop-color="#eaf2f9"/>
      </linearGradient>
    </defs>
    <rect width="779" height="230" fill="url(#haze)"/>
    <path d="M0 0 H779 V120 C640 150 520 170 420 178 C300 188 160 170 0 150 Z" fill="url(#band)"/>
    <path d="M0 170 C180 195 330 205 460 190 C600 175 700 150 779 128 V150 C700 170 590 195 460 205 C320 215 170 210 0 196 Z" fill="#ffffff" opacity="0.75"/>
  </svg>

  <div class="brand">
    <span class="brand-dot"></span>
    <span class="brand-name">Tarewa<br>Holiday Park</span>
  </div>
  <div class="tagline">Cabins and Camping</div>

  <div class="contact">
    <div class="web">www.tarewaholidaypark.co.nz</div>
    <div class="phone">Free phone:&nbsp; 0800 555 0192</div>
    <div class="address">12 Kowhai Lane<br>Tarewa , Northland</div>
  </div>

  <div class="photo-column">
    <div class="photo photo-harbour" role="img" aria-label="Couple reading a newspaper at a picnic table beside a boat, harbour view behind"></div>
    <div class="photo photo-playground" role="img" aria-label="Wooden children's playground with slide and swings"></div>
    <div class="photo photo-cabin" role="img" aria-label="Holiday cabin on a green lawn with flowering agapanthus"></div>
    <div class="photo photo-campground" role="img" aria-label="Campground with caravans and palms, harbour in the distance"></div>
    <div class="photo photo-sunset" role="img" aria-label="Fiery orange sunset sky over silhouetted trees"></div>
  </div>

  <svg class="swoosh" viewBox="0 0 110 1000" aria-hidden="true">
    <path d="M40 0 H74 C60 300 96 600 64 1000 H30 C62 600 26 300 40 0 Z" fill="var(--swoosh-lime)"/>
    <path d="M50 0 H80 C66 300 102 600 72 1000 H46 C76 600 40 300 50 0 Z" fill="var(--swoosh-green)"/>
    <path d="M62 0 H86 C72 300 106 600 80 1000 H62 C90 600 54 300 62 0 Z" fill="var(--swoosh-blue)" opacity="0.85"/>
    <path d="M70 0 H74 C62 300 96 600 70 1000 H66 C92 600 58 300 70 0 Z" fill="#ffffff" opacity="0.8"/>
  </svg>

  <section class="attractions">
    <h2>Fun activities &amp; attractions just a short drive from Tarewa Holiday Park:</h2>
    <ul>
      <li>Head 15 minutes towards Dargaville you'll find Tokatoka Peak. A moderate hike to the top and what a view!</li>
      <li>20 minutes to Pahi for another seaside village, wharf and one of the largest Moreton Bay Fig trees you will ever see</li>
      <li>5 minutes to Paparoa where you'll find a pub, shops, restaurants and a nice creek-side walking track</li>
      <li>5 minutes to the Kauri Bushman's reserve to view our local Kauri tree</li>
      <li>And if you don't want to drive any where, relax in our Tarewa Holiday Park and admire the view and enjoy the peace and quiet</li>
      <li>Only a short stroll to Tarewa's own Shelly Beach, or visit the local cafes and Timber Heritage Museum (A must see attraction - allow 2-4 Hrs. )</li>
    </ul>
  </section>

  <p class="closing">So for great Northland camping and holiday park accommodation, visit Tarewa Holiday Park. Here on the Two Harbours Touring Route, this is where the water meets the land and the adventure starts!</p>

  <div class="call-to-action">Book your accommodation now!</div>
</div>
</body>
</html>
```